Skin cancer clinic services trifold brochure

Need trifold brochure listing skin cancer services our clinic provides, staff information, location and brief about skin cancer with colours similar to our web site www.Dermavoy.clinic. I will provide more information regarding services and staff but want this colourful and standout as it will be given to other referring doctors or patients
Updates

Target Market(s)

Age 40 to 80 years

Industry/Entity Type

Medical

Font styles to use
Serif

Colors

Designer to choose colors to be used in the design.

Requirements
Must have
• Logo, services, contact info, beach or sun look and colours similar to web site or logo

```html
<!DOCTYPE html>
<html lang="en">
<head>
<meta charset="utf-8">
<title>Dermavoy Trifold Brochure</title>
<link href="https://fonts.googleapis.com/css2?family=Lora:ital,wght@0,400;0,600;0,700;1,400&display=swap" rel="stylesheet">
<style>
:root{
  --bg:#6b6c6f;
  --orange:#e0661f;
  --orange-deep:#c9380b;
  --red:#b8270a;
  --amber:#efa21f;
  --yellow:#f2b53a;
  --ink:#2c2420;
  --text:#3b3330;
  --white:#ffffff;
  --sheet-shadow:0 14px 22px rgba(0,0,0,.35);
}
*{margin:0;padding:0;box-sizing:border-box}
html,body{width:1200px;height:1200px;overflow:hidden}
body{background:var(--bg);font-family:"Lora",Georgia,serif;color:var(--text);position:relative}
h1,h2,h3,h4,h5{font-weight:400}
.sheet{position:absolute;left:237px;width:726px;height:514px;background:var(--white);box-shadow:var(--sheet-shadow);overflow:hidden}
.sheet--outside{top:59px}
.sheet--inside{top:629px}
.panel{position:absolute;top:0;height:100%}
.abs{position:absolute}
.placeholder{position:absolute}

/* Outside: team */
.team{left:0;width:237px;background:var(--white)}
.team__title{left:16px;top:16px;font-size:15px;font-weight:700;color:var(--orange)}
.team__rule{left:97px;top:24px;width:140px;height:6px;background:var(--orange)}
.team__photo{left:0;top:50px;width:237px;height:117px;background:linear-gradient(135deg,#e9eef2,#bfc8cf 60%,#dfe4e8)}
.team__photo-bar{left:0;top:167px;width:237px;height:6px;background:var(--orange)}
.bio{position:absolute;left:15px;width:215px;font-size:6px;line-height:1.5;color:var(--text)}
.bio h4{font-size:7.5px;font-weight:600;color:var(--orange);display:inline-block;padding-bottom:2px;border-bottom:2px solid var(--ink);margin-bottom:4px}
.bio--right{text-align:right}
.team__foot{left:0;bottom:0;width:237px;height:16px;background:linear-gradient(90deg,var(--amber) 50%,var(--orange) 50%)}

/* Outside: intro */
.intro{left:237px;width:245px;background:linear-gradient(180deg,var(--orange) 0,var(--orange) 269px,var(--amber) 269px,var(--yellow) 100%);text-align:center}
.intro__title{left:0;right:0;top:28px;font-size:17px;font-weight:700;line-height:1.25;color:var(--ink)}
.intro__copy{left:28px;right:28px;top:90px;font-size:8.6px;line-height:1.45;color:var(--ink)}
.intro__copy p+p{margin-top:12px}
.intro__frame{left:24px;top:201px;width:199px;height:182px;background:var(--amber)}
.intro__photo{left:30px;top:209px;width:191px;height:174px;background:linear-gradient(180deg,#8fa4ae,#5f7380 45%,#a67456 70%,#2e4d68)}
.contact{left:0;right:0;top:406px;color:var(--ink)}
.contact h3{font-size:12.5px}
.contact__addr{font-size:8.5px;line-height:1.15;margin-top:9px}
.contact__phone{font-size:13px;margin-top:6px}
.contact__mail{font-size:8.5px;margin-top:8px}

/* Outside: cover */
.cover{left:482px;width:244px;background:linear-gradient(180deg,#f2b9a0 0%,#f4a57c 22%,#e9a79a 45%,#b9a5b2 65%,#6f7888 85%,#4c5564 100%)}
.cover__brand{left:0;right:0;top:142px;text-align:center;font-size:26px;font-weight:700;color:var(--white)}
.cover__tag{left:0;right:0;top:380px;text-align:center;font-size:21px;font-style:italic;line-height:1.2;color:var(--white)}

/* Inside */
.bands{position:absolute;left:0;top:0}
.services{left:0;width:238px}
.label{position:absolute;background:var(--amber);color:var(--ink);padding:1px 8px 1px 19px}
.label::before{content:"";position:absolute;left:0;top:0;bottom:0;width:6px;background:var(--orange)}
.label--services{left:0;top:82px;font-size:14px;width:193px}
.label--treat{left:0;top:282px;font-size:10.5px;width:104px}
.list{list-style:none;position:absolute}
.list li{display:flex;align-items:center;gap:7px;color:var(--ink)}
.list svg{width:13px;height:13px;flex:none}
.list--services{left:17px;top:108px;font-size:11px}
.list--services li{height:24px}
.treat{position:absolute;left:19px;width:200px;font-size:5.6px;line-height:1.5;color:var(--text)}
.treat h5{font-size:8px;color:var(--orange);margin-bottom:1px}

.devices{left:238px;width:250px;text-align:center}
.devices__title{left:0;right:0;top:86px;font-size:14.5px;color:var(--orange)}
.devices__copy{left:26px;right:26px;top:113px;font-size:8px;line-height:1.45;color:var(--ink)}
.list--devices{top:160px;font-size:9.5px;text-align:left}
.list--devices li{height:20px;gap:8px}
.list--a{left:15px}
.list--b{left:131px;padding-left:9px;border-left:2px solid var(--amber)}
.devices__tech{left:0;right:0;top:296px;font-size:11px;line-height:1.38;color:var(--ink)}
.devices__cta{left:28px;right:28px;top:380px;font-size:8px;line-height:1.5;color:var(--orange)}
.devices__cta p+p{margin-top:6px}

.about{left:488px;width:238px}
.about__title{left:30px;top:117px;font-size:14.5px;color:var(--orange)}
.about__copy{left:30px;width:195px;top:150px;font-size:8px;line-height:1.45;color:var(--ink)}
.about__copy p+p{margin-top:10px}
.about__diagram{left:40px;top:262px;width:160px;height:160px;background:radial-gradient(ellipse at 50% 55%,#f0a184,#eebf78 55%,rgba(255,255,255,0) 72%)}
</style>
</head>
<body>
<svg width="0" height="0" style="position:absolute" aria-hidden="true">
  <symbol id="sun" viewBox="0 0 20 20">
    <g fill="none" stroke="#e78a2c" stroke-width="1.1" stroke-linecap="round">
      <circle cx="10" cy="10" r="4.2"/>
      <path d="M10 1v3M10 16v3M1 10h3M16 10h3M3.6 3.6l2.1 2.1M14.3 14.3l2.1 2.1M3.6 16.4l2.1-2.1M14.3 5.7l2.1-2.1"/>
    </g>
  </symbol>
</svg>

<section class="sheet sheet--outside">
  <div class="panel team">
    <h2 class="abs team__title">Our Team</h2>
    <div class="abs team__rule"></div>
    <div class="placeholder team__photo" role="img" aria-label="Photo of a clinician in a mask and lab coat examining a sample"></div>
    <div class="abs team__photo-bar"></div>
    <div class="bio" style="top:186px"><h4>Dr. Maren Colby</h4><p>BMed. FRACGP. Diploma Skin Cancer Medicine/Surgery. Diploma Aesthetic Medicine. Born in the USA. Maren gained her medical degree at Harbourside University. Dr. Colby enjoys the Outdoors, Gardening, Family, Boating, and Holidays. Professional interests include Skin Care, Cosmetic Treatments.</p></div>
    <div class="bio bio--right" style="top:257px"><h4>Dr. Tessa Varrow</h4><p>BMed. FRACGP. Diploma Skin Cancer Medicine/Surgery. Born in Australia. Dr. Varrow enjoys the Outdoors, Gardening, Family, Beach, and Holidays. Professional interests include Skin Care &amp; Cosmetic Treatments, Family Medicine.</p></div>
    <div class="bio" style="top:317px"><h4>Dr. Lena Hartfield</h4><p>MBBS. Born in the USA and moved to Australia in 2004, Lena completed her Medical Degree at Eastcoast University. NSW. In 2004. Dr. Hartfield enjoys Running, Fitness, Spending quality time with family and visiting the beach. Professional interests include Skin Care, Cosmetic Treatments and Family Medicine.</p></div>
    <div class="bio bio--right" style="top:392px"><h4>Orla Penrick</h4><p>Registered Nurse: ACNEM Certificate in Nutritional and Environmental Medicine<br>Medi Cosmetic Nurse: Orla is our Cosmetic Specialist and is available by appointment.</p></div>
    <div class="bio" style="top:451px"><h4>Ivy Calder</h4><p>Registered Nurse: Ivy is our Laser Treatment Specialist and is available via appointment</p></div>
    <div class="abs team__foot"></div>
  </div>

  <div class="panel intro">
    <h1 class="abs intro__title">When was your<br>last check?</h1>
    <div class="abs intro__copy">
      <p>Dermavoy is a leading coastal skin cancer clinic based in Wattle Bay.</p>
      <p>Headed by qualified professional Dr Maren Colby, Dermavoy engages the latest technology and clinical care to identify the best treatments and preventative measures for clients.</p>
    </div>
    <div class="abs intro__frame"></div>
    <div class="placeholder intro__photo" role="img" aria-label="Photo of a woman seen from behind, sitting on a boat looking at a coastal town"></div>
    <div class="abs contact">
      <h3>Contact Us</h3>
      <p class="contact__addr">Suites 3 &amp; 4 118 Shoreline Road<br>Wattle Bay NSW 2299</p>
      <p class="contact__phone">1300 555 014</p>
      <p class="contact__mail">hello@dermavoy.clinic</p>
    </div>
  </div>

  <div class="panel cover placeholder" role="img" aria-label="Photo of a sunset over a calm beach with rocks in the shallows">
    <p class="abs cover__brand">Dermavoy</p>
    <p class="abs cover__tag">Comfort<br>In Your Skin</p>
  </div>
</section>

<section class="sheet sheet--inside">
  <svg class="bands" width="726" height="514" viewBox="0 0 726 514" aria-hidden="true">
    <polygon points="0,0 726,0 726,42 610,78 488,94 238,34 0,58" fill="#c9380b"/>
    <polygon points="0,58 238,34 488,94 610,78 726,42 726,46 488,100 238,40 0,70" fill="#efa21f"/>
    <polygon points="0,70 238,40 488,100 726,46 726,58 488,108 238,46 0,86" fill="#f2b53a"/>
    <polygon points="0,0 238,0 238,34 0,58" fill="#d8500f"/>
    <polygon points="0,478 238,430 488,484 726,438 726,514 0,514" fill="#efa21f"/>
    <polygon points="0,484 238,436 488,490 726,444 726,514 0,514" fill="#e0661f"/>
    <polygon points="0,492 238,444 488,498 726,452 726,514 0,514" fill="#c9380b"/>
    <polygon points="238,444 488,498 488,514 238,514" fill="#d04410"/>
  </svg>

  <div class="panel services">
    <h2 class="label label--services">Our specialised services</h2>
    <ul class="list list--services">
      <li><svg><use href="#sun"/></svg>Skin cancer detection</li>
      <li><svg><use href="#sun"/></svg>Mole assessment</li>
      <li><svg><use href="#sun"/></svg>Digital monitoring of moles</li>
      <li><svg><use href="#sun"/></svg>Medical treatment of skin cancer</li>
      <li><svg><use href="#sun"/></svg>Surgical treatment of skin cancer</li>
      <li><svg><use href="#sun"/></svg>General dermatologic surgery</li>
      <li><svg><use href="#sun"/></svg>Same day ‘slow MOHs’ procedures</li>
    </ul>
    <h3 class="label label--treat">TREATMENTS</h3>
    <div class="treat" style="top:303px"><h5>EXCISION</h5><p>Best treatment for the majority of skin cancers,<br>including melanoma.</p></div>
    <div class="treat" style="top:339px"><h5>CURETTAGE</h5><p>This traditional treatment is highly effective<br>on many superficial skin cancers.</p></div>
    <div class="treat" style="top:375px"><h5>CRYOSURGERY</h5><p>Cryosurgery – also known as cryotherapy – applies liquid nitrogen directly to the skin. The extremely cold temperature destroys abnormal skin cells, effectively freezing the abnormality off.</p></div>
  </div>

  <div class="panel devices">
    <h2 class="abs devices__title">Devices and Services</h2>
    <p class="abs devices__copy">Our mission is to help people with a range of conditions, with our advanced technology &amp; well trained staff.</p>
    <ul class="list list--devices list--a">
      <li><svg><use href="#sun"/></svg>Veins</li>
      <li><svg><use href="#sun"/></svg>Rosacea</li>
      <li><svg><use href="#sun"/></svg>Wrinkles</li>
      <li><svg><use href="#sun"/></svg>Large Pores</li>
      <li><svg><use href="#sun"/></svg>Acne Scarring</li>
      <li><svg><use href="#sun"/></svg>Hair Removal</li>
    </ul>
    <ul class="list list--devices list--b">
      <li><svg><use href="#sun"/></svg>Poor Skin Texture</li>
      <li><svg><use href="#sun"/></svg>Sun Damaged Skin</li>
      <li><svg><use href="#sun"/></svg>Skin Rejuvenation</li>
      <li><svg><use href="#sun"/></svg>Unwanted Scars</li>
      <li><svg><use href="#sun"/></svg>Skin Blemishes</li>
      <li><svg><use href="#sun"/></svg>Pigmentation</li>
    </ul>
    <p class="abs devices__tech">Yag Laser<br>Sunray IPL<br>Laser Renew<br>Opal/Opal Fractional<br>Tide Wave</p>
    <div class="abs devices__cta">
      <p>Do you have a suspicious lesion that you need evaluated immediately?</p>
      <p>GET CHECKED TODAY!</p>
    </div>
  </div>

  <div class="panel about">
    <h2 class="abs about__title">What is Skin Cancer?</h2>
    <div class="abs about__copy">
      <p>Skin cancer — the abnormal growth of skin cells — most often develops on skin exposed to the sun. But this common form of cancer can also occur on areas of your skin not ordinarily exposed to sunlight.</p>
      <p>There are three major types of skin cancer — basal cell carcinoma, squamous cell carcinoma and melanoma.</p>
    </div>
    <div class="placeholder about__diagram" role="img" aria-label="Illustration of a cross-section of skin layers with a tumour and hair follicles"></div>
  </div>
</section>
</body>
</html>
```